Stationery Design Project for Marketing Consultancy

I have started a new consultancy business and require the following elements to be designed using existing logo:
• Business card
• Letterhead
• Envelope (DL, C4, C5)
• Microsoft word template for report writing
• A4 Presentation Folder
• Powerpoint template
COPY FOR FRONT AND BACK OF BUSINESS CARD
logo
'Countable Growth. Bold Outcomes' slogan (but no need to use existing lockup with logo)
name, B Bus. Mktg, Grad Dip Digital Mktg, CPM (post nominal abbreviations in smaller font)
mobile: 04XX-XXX-XXX (I will give details to the winner to add)
website: www.quorvale.com.au
email: info@quorvale.com.au
COPY FOR LETTERHEAD
Logo
Company Name
Please, submit your designs that include business card, letterhead and envelope. Once selected the winner will be asked to complete the project by creating the rest of the artwork.
FINAL FILES
Print ready files to be supplied as well as Indesign files so that minor amends can be made if necessary in future.
• Layered vectors in EPS & PDF
• Screen quality JPEG & PNGs
ABOUT THE BUSINESS: QUORVALE
I work with clients to understand their business challenges, developing and executing measurable marketing strategies tied to key business metrics. Services include:
Services include:
• Business planning and business development
• Marketing and brand strategy
• Insight-driven integrated campaigns
• Loyalty programs and retention marketing
• Marketing automation
• Direct marketing (traditional and digital)
• Content strategy and development
Hi everyone,
Target Market(s)
Corporate decision makers (heads of marketing, general managers etc) and small to medium sized business owners. Predominately male aged 35+
Industry/Entity Type
Marketing
Requirements
Must have
- BRAND PERSONALITY
The successful design will communicate brand personality. I am a professional, results-driven entrepreneur, but want to show off my creative flair.
MEMORABILITY
Looking for a unique and eye-catching design. Am considering special printing effects (die cuts, letterpress, interactive elements, embossing, foiling etc) or a striking minimalist approach.
Nice to have
- I have a mission that could be incorporated on reverse if room -
Turning insights into actions & passion into profit.
Should not have
- Use of pink or green.

```html
<!DOCTYPE html>
<html lang="en">
<head>
<meta charset="utf-8">
<title>Quorvale Stationery Set</title>
<link rel="stylesheet" href="https://fonts.googleapis.com/css2?family=Crimson+Text:wght@400;600&family=Dancing+Script:wght@500&family=Open+Sans:wght@400&display=swap">
<style>
  :root {
    --stage: #000000;
    --paper: #fdfdfc;
    --ink: #3a3a3a;
    --brand: #3b3b3b;
    --teal: #2a93a8;
    --teal-deep: #1f8ea4;
    --gold: #f2c55c;
    --gold-soft: #e9c27a;
    --muted: #555555;
  }
  * { margin: 0; padding: 0; box-sizing: border-box; }
  html, body { width: 1200px; height: 857px; overflow: hidden; background: var(--stage); }
  .stage { position: relative; width: 1200px; height: 857px; background: var(--stage); }

  .sheet { position: absolute; background: var(--paper); overflow: hidden; }
  .serif { font-family: "Crimson Text", Georgia, serif; }
  .script { font-family: "Dancing Script", cursive; }
  .sans { font-family: "Open Sans", Arial, sans-serif; }

  .brand-name {
    position: absolute; font-family: "Crimson Text", Georgia, serif;
    font-weight: 600; color: var(--brand); letter-spacing: 0.04em; white-space: nowrap;
  }
  .brand-dot { position: absolute; border-radius: 50%; background: var(--brand); }

  .totem { position: absolute; }

  /* Letterhead */
  .letterhead { left: 55px; top: 60px; width: 518px; height: 693px; }
  .letterhead .brand-dot { left: 248px; top: 28px; width: 26px; height: 26px; }
  .letterhead .brand-name { left: 0; width: 518px; text-align: center; top: 62px; font-size: 18px; }
  .letterhead .mission {
    position: absolute; left: 0; width: 526px; text-align: center; top: 88px;
    font-size: 13px; color: #222;
  }
  .letterhead .totem-row { left: 197px; top: 103px; width: 120px; height: 28px; }
  .letterhead .totem-side { left: 438px; top: 320px; width: 80px; height: 373px; }
  .letterhead .contact {
    position: absolute; left: 25px; top: 620px; font-size: 10px; line-height: 12px; color: var(--gold);
  }

  /* Business card */
  .card {
    left: 607px; top: 80px; width: 538px; height: 310px;
    background:
      radial-gradient(ellipse 120px 150px at 445px 120px, var(--teal-deep) 0%, rgba(31,142,164,0.85) 40%, rgba(31,142,164,0.25) 80%, rgba(31,142,164,0) 100%),
      linear-gradient(90deg, #f1f9fb 0%, #e6f4f7 45%, #9fd3de 100%);
  }
  .card .brand-dot { left: 262px; top: 46px; width: 30px; height: 30px; }
  .card .brand-name { left: 220px; width: 120px; text-align: center; top: 98px; font-size: 19px; }
  .card .mission { position: absolute; left: 158px; top: 134px; font-size: 12.5px; color: var(--ink); }
  .card .totem-side { left: 38px; top: 35px; width: 76px; height: 275px; }
  .card .contact {
    position: absolute; left: 329px; top: 215px; font-size: 10px; line-height: 11.5px; color: var(--ink);
  }
  .card .contact small { font-size: 7px; }
  .card .contact .email { color: var(--gold); }

  /* Envelope */
  .envelope { left: 597px; top: 486px; width: 582px; height: 267px; background: #ffffff; }
  .envelope .brand-dot { left: 50px; top: 28px; width: 18px; height: 18px; }
  .envelope .brand-name { left: 36px; top: 56px; font-size: 11px; }
  .envelope .sender {
    position: absolute; left: 37px; top: 75px; font-size: 5.5px; line-height: 10px; color: #222;
  }
  .envelope .totem-side { left: 243px; top: 88px; width: 48px; height: 138px; }
  .envelope .recipient { position: absolute; left: 292px; font-size: 7.5px; color: #222; }
  .envelope .r-name { top: 145px; }
  .envelope .r-address { top: 171px; }
  .envelope .r-city { top: 198px; }
  .envelope .mission {
    position: absolute; right: 30px; top: 236px; font-size: 8px; color: var(--gold-soft);
  }
</style>
</head>
<body>
<main class="stage">

  <section class="sheet letterhead" aria-label="Letterhead">
    <span class="brand-dot"></span>
    <span class="brand-name">QUORVALE</span>
    <p class="mission script">Turning insights into actions &amp; passion into profit.</p>
    <svg class="totem totem-row" role="img" aria-label="Row of teal and gold pentagon blocks" viewBox="0 0 120 28" preserveAspectRatio="none">
      <defs>
        <linearGradient id="rowFill" x1="0" y1="0" x2="1" y2="1">
          <stop offset="0" stop-color="#2a93a8"/>
          <stop offset="0.6" stop-color="#2a93a8"/>
          <stop offset="1" stop-color="#f2c55c"/>
        </linearGradient>
      </defs>
      <rect width="120" height="28" rx="6" fill="url(#rowFill)"/>
    </svg>
    <svg class="totem totem-side" role="img" aria-label="Stacked teal and gold pentagon tower with ribbon" viewBox="0 0 80 373" preserveAspectRatio="none">
      <defs>
        <linearGradient id="sideFill" x1="0" y1="0" x2="0" y2="1">
          <stop offset="0" stop-color="#f2c55c"/>
          <stop offset="0.25" stop-color="#e7c068"/>
          <stop offset="0.4" stop-color="#2a93a8"/>
          <stop offset="1" stop-color="#2a8aa0"/>
        </linearGradient>
      </defs>
      <rect width="80" height="373" rx="10" fill="url(#sideFill)"/>
    </svg>
    <div class="contact serif">
      <p>Logo</p>
      <p>Company Name</p>
      <p>mobile: 04XX-XXX-XXX (winner to add)</p>
      <p>website: www.quorvale.com.au</p>
      <p>email: info@quorvale.com.au</p>
    </div>
  </section>

  <section class="sheet card" aria-label="Business card">
    <svg class="totem totem-side" role="img" aria-label="Stacked gold and teal pentagon tower with ribbon" viewBox="0 0 76 275" preserveAspectRatio="none">
      <defs>
        <linearGradient id="cardFill" x1="0" y1="0" x2="0" y2="1">
          <stop offset="0" stop-color="#2a93a8"/>
          <stop offset="0.3" stop-color="#eec06a"/>
          <stop offset="0.5" stop-color="#2a93a8"/>
          <stop offset="0.72" stop-color="#f2c55c"/>
          <stop offset="1" stop-color="#1f8ea4"/>
        </linearGradient>
      </defs>
      <rect width="76" height="275" rx="10" fill="url(#cardFill)"/>
    </svg>
    <span class="brand-dot"></span>
    <span class="brand-name">QUORVALE</span>
    <p class="mission serif">Turning insights into actions &amp; passion into profit.</p>
    <div class="contact serif">
      <p>Countable Growth. Bold Outcomes</p>
      <p>name, Bus. <small>Mktg, Grad Dip Digital Mktg, CPM</small></p>
      <p>mobile: 04XX-XXX-XXX</p>
      <p>website: www.quorvale.com.au</p>
      <p class="email">email: info@quorvale.com.au</p>
    </div>
  </section>

  <section class="sheet envelope" aria-label="DL envelope">
    <span class="brand-dot"></span>
    <span class="brand-name">QUORVALE</span>
    <div class="sender sans">
      <p>Address</p>
      <p>mobile: 04XX-XXX-XXX</p>
      <p>website: www.quorvale.com.au</p>
    </div>
    <svg class="totem totem-side" role="img" aria-label="Small stacked pentagon tower with ribbon" viewBox="0 0 48 138" preserveAspectRatio="none">
      <defs>
        <linearGradient id="envFill" x1="0" y1="0" x2="0" y2="1">
          <stop offset="0" stop-color="#2a93a8"/>
          <stop offset="0.35" stop-color="#e9c27a"/>
          <stop offset="0.6" stop-color="#2a93a8"/>
          <stop offset="1" stop-color="#f2c55c"/>
        </linearGradient>
      </defs>
      <rect width="48" height="138" rx="8" fill="url(#envFill)"/>
    </svg>
    <p class="recipient r-name sans">Name</p>
    <p class="recipient r-address sans">Address</p>
    <p class="recipient r-city sans">City, State, ZIP</p>
    <p class="mission script">Turning insights into actions &amp; passion into profit</p>
  </section>

</main>
</body>
</html>
```